Uprising SaaS company needs an attractive business card design

We're an uprising SaaS company who's attempting to attack the rigid car (insurance) claims management market in Europe.
We want to our mighty base order management system, listen to our clients to connect the smart ideas to build something even mightier.
We primarily focus on helping our customers manage their customers' claims/orders and get them resolved as smoothly as possible.
We'd like the business card design to express technical innovation and the fact that we connect smart ideas, as our company slogan indicates.
Contact Information for Business Card
Name, position, website, email, mobile, business address
Colors
Designer to choose colors to be used in the design.
Look and feel
Each slider illustrates characteristics of the customer's brand and the style your logo design should communicate.

```html
<!DOCTYPE html>
<html lang="en">
<head>
<meta charset="utf-8">
<title>veltrano business card</title>
<link href="https://fonts.googleapis.com/css2?family=Arimo:wght@400;700&display=swap" rel="stylesheet">
<style>
  :root {
    --backdrop: #e7e7e5;
    --card: #7d7d7d;
    --card-edge: #8a8a8a;
    --ink: #ffffff;
    --accent: #7ccbe6;
    --emboss: #6a6a6a;
  }
  * { margin: 0; padding: 0; box-sizing: border-box; }
  html, body {
    width: 1200px; height: 802px; overflow: hidden;
    background: var(--backdrop);
    font-family: "Arimo", Arial, sans-serif;
  }
  .stage { position: relative; width: 1200px; height: 802px; }
  .card {
    position: absolute; width: 520px; height: 300px;
    background: var(--card);
    border-top: 1px solid var(--card-edge);
  }
  .card--front { left: 70px; top: 110px; }
  .card--back { left: 610px; top: 392px; }

  .wordmark {
    position: absolute; font-weight: 400; letter-spacing: 1px; line-height: 1;
  }
  .card--front .wordmark {
    right: 34px; top: 70px; font-size: 66px; color: var(--ink);
  }
  .card--back .wordmark {
    left: 0; right: 0; top: 112px; text-align: center;
    font-size: 76px; color: var(--emboss);
  }

  .divider {
    position: absolute; left: 200px; right: 30px; top: 176px;
    height: 1px; background: var(--ink);
  }

  .person { position: absolute; left: 30px; top: 160px; }
  .person__name { font-weight: 700; font-size: 17px; color: var(--accent); }
  .person__role { font-size: 13px; color: var(--ink); margin-top: 3px; }
  .person__rule { width: 140px; height: 1px; background: var(--ink); margin-top: 9px; }

  .contact { position: absolute; left: 30px; top: 218px; list-style: none; }
  .contact li {
    display: flex; align-items: center; gap: 9px;
    font-size: 13px; color: var(--ink); height: 20px;
  }
  .contact svg { width: 11px; height: 11px; flex: none; }

  .address {
    position: absolute; right: 30px; top: 190px; text-align: right;
    font-size: 13px; line-height: 19px; color: var(--ink);
  }
</style>
</head>
<body>
<div class="stage">

  <section class="card card--front" aria-label="Business card front">
    <div class="wordmark">veltrano</div>
    <div class="divider"></div>

    <div class="person">
      <div class="person__name">Jonas Redeker</div>
      <div class="person__role">CEO</div>
      <div class="person__rule"></div>
    </div>

    <ul class="contact">
      <li>
        <svg viewBox="0 0 12 12" aria-hidden="true"><path d="M3 1 L5 3.5 L4 5 Q5.5 7.5 7 8 L8.5 7 L11 9 L9.5 11 Q4 10.5 1 3 Z" fill="var(--accent)"/></svg>
        123-555-0148
      </li>
      <li>
        <svg viewBox="0 0 12 12" aria-hidden="true"><rect x="1" y="2.5" width="10" height="7" fill="none" stroke="var(--accent)" stroke-width="1.2"/><path d="M1 2.5 L6 6.5 L11 2.5" fill="none" stroke="var(--accent)" stroke-width="1.2"/></svg>
        info@veltrano.com
      </li>
      <li>
        <svg viewBox="0 0 12 12" aria-hidden="true"><circle cx="6" cy="6" r="5" fill="var(--accent)"/><path d="M1 6 H11 M6 1 Q3 6 6 11 M6 1 Q9 6 6 11" fill="none" stroke="var(--card)" stroke-width="0.8"/></svg>
        www.veltrano.com
      </li>
    </ul>

    <div class="address">
      veltrano GmbH<br>
      Lindenweg 14b<br>
      10115 Berlin - Germany
    </div>
  </section>

  <section class="card card--back" aria-label="Business card back">
    <div class="wordmark">veltrano</div>
  </section>

</div>
</body>
</html>
```